Re jig a A4 Instructional Flyer

We need an established A4 instructional Flyer (2 pages x A4) - to be rejigged in Harlow Academy of Learning Branding to look fresh and new.

Permissions have been received to rejig this Medical Triage Chart. Fresh branding and setting out (fonts) required.

FOOTER NOTES : to be inserted at the bottom of the A4 instruction sheet

Harlow Academy produced with permissions from Coastal Care Alliance, produced by Coastal Care Alliance with Clinic Circle Eastgate with permissions from Southern Basin Careline Hub. Harlow acknowledges the FMPCB Standards Criterion 3.2.3 Practice Training and Education in Triage

Target Market(s)

Medical Practices

Industry/Entity Type

Health

Font styles to use
Serif

Colors
0255a3
f78f20

Requirements
Must have
• Professional
• Pops of colour in the chart.
• This chart is to be USED and is VISUAL (no boring grey words throughout)
• PROBS SANS SERIF but SERIF for titles OK
Nice to have
• look at www.harlowlearning.edu.au FOR BRANDING look and feel

```html
<!DOCTYPE html>
<html lang="en">
<head>
<meta charset="utf-8">
<title>Triage – Harlow Academy of Learning</title>
<link href="https://fonts.googleapis.com/css2?family=Montserrat:wght@500;700&family=Source+Sans+3:ital,wght@0,400;0,600;0,700;1,400;1,600;1,700&display=swap" rel="stylesheet">
<style>
:root{
  --brand-blue:#0255a3;
  --brand-orange:#f78f20;
  --charcoal:#3b3b3d;
  --band:#dde3ec;
  --gold:#f6be1a;
  --cat1:#e3101e;
  --cat2:#f78f20;
  --cat3:#f6be1a;
  --cat4:#12a39a;
  --cat5:#5b2a8a;
  --cat6:#7fa61f;
  --tan:#f3c998;
  --line:#7a7a7a;
  --ink:#1f1f1f;
}
*{box-sizing:border-box;margin:0;padding:0}
html,body{width:1200px;height:848px;overflow:hidden;background:#fff}
body{position:relative;font-family:"Source Sans 3",sans-serif;color:var(--ink);font-size:13px;line-height:17px}
.header-band{position:absolute;left:0;top:0;width:1200px;height:128px;background:var(--band)}
.brand-block{position:absolute;left:26px;top:0;width:309px;height:128px;background:var(--brand-blue)}
.brand-mark{position:absolute;left:14px;top:13px;width:108px;height:100px;background:#fff;display:flex;align-items:center;justify-content:center;text-align:center;padding:8px;font-size:12px;line-height:14px;font-weight:600;color:var(--brand-blue)}
.title{position:absolute;left:149px;top:40px;font-family:"Montserrat",sans-serif;font-weight:700;font-size:38px;line-height:44px;color:#fff;letter-spacing:.5px}
.subtitle{position:absolute;left:362px;top:48px;font-family:"Montserrat",sans-serif;font-weight:500;font-size:18px;line-height:21px;color:#222}
.action-plan{position:absolute;left:916px;top:0;width:254px;height:319px;background:var(--charcoal);color:#fff;padding:38px 20px 0 22px}
.action-plan h2{font-family:"Montserrat",sans-serif;font-weight:700;font-size:14px;white-space:nowrap;color:var(--brand-orange);display:flex;align-items:center;gap:8px;margin-bottom:8px}
.alert-dot{width:20px;height:20px;border-radius:50%;background:var(--brand-orange);color:var(--charcoal);font-size:13px;display:flex;align-items:center;justify-content:center;flex:none}
.action-plan li{list-style:none;font-size:14px;line-height:20px;padding:6px 0 5px;border-bottom:1px solid #9a9a9a}
.action-plan li.call{border:none;color:var(--brand-orange);font-style:italic;font-weight:600;padding-top:7px}
.flow-question{position:absolute;left:29px;top:170px;width:132px;height:71px;border:1.5px solid var(--brand-blue);font-style:italic;font-size:13.5px;line-height:17px;text-align:center;padding-top:8px}
.flow-urgent{position:absolute;left:303px;top:177px;width:144px;height:58px;background:var(--brand-blue);color:#fff;font-weight:700;font-size:14px;line-height:17px;text-align:center;padding-top:11px}
.flow-lines{position:absolute;left:0;top:0}
.flow-label{position:absolute;font-style:italic;font-size:13.5px}
.record{position:absolute;left:556px;top:174px;font-size:13.5px}
.record h3{font-weight:700;font-size:14px;margin-bottom:2px}
.record li{margin-left:12px;line-height:17px}
.triage-table{position:absolute;left:30px;top:337px;width:1142px;display:grid;grid-template-columns:148px repeat(6,1fr);grid-template-rows:34px 224px 72px 51px 57px;border:1px solid var(--line)}
.cell{border-right:1px solid var(--line);border-bottom:1px solid var(--line);padding:9px 11px;position:relative}
.cell:nth-child(7n){border-right:none}
.cell.has-flag{padding-right:34px}
.head{display:flex;align-items:center;justify-content:center;font-weight:700;font-style:italic;font-size:14.5px;color:#fff;padding:0}
.head.instruction{justify-content:flex-start;padding-left:12px;color:var(--ink);font-size:13px}
.c1{background:var(--cat1)}.c2{background:var(--cat2)}.c3{background:var(--cat3)}.c4{background:var(--cat4)}.c5{background:var(--cat5)}.c6{background:var(--cat6)}
.row-label{font-weight:700;font-style:italic}
.symptoms ul{margin-left:13px}
.symptoms li{line-height:17px}
.tell{background:var(--brand-blue);color:#fff;border-color:#01457f}
.tell.bold{font-weight:600}
.notify{background:var(--band)}
.notify.bold{font-weight:600}
.records{background:var(--tan);border-bottom:none}
.flag{position:absolute;right:10px;top:9px;width:17px;height:17px;border-radius:50%;background:#fff;color:var(--brand-blue);font-weight:700;font-size:12px;display:flex;align-items:center;justify-content:center}
.notify .flag{background:var(--brand-orange);color:#fff}
.footer{position:absolute;left:43px;top:795px;display:flex;gap:10px;align-items:flex-start}
.footer-mark{width:58px;display:flex;align-items:flex-start;gap:3px;font-size:7px;line-height:8px;font-weight:700;color:var(--brand-blue)}
.footer-mark span.sq{width:6px;height:6px;background:var(--brand-orange);flex:none;margin-top:1px}
.footer p{font-size:7.2px;line-height:12.5px;color:#222}
</style>
</head>
<body>
<div class="header-band"></div>
<div class="brand-block">
  <div class="brand-mark">Harlow Academy of Learning</div>
  <div class="title">TRIAGE</div>
</div>
<div class="subtitle">A guide to urgency for non-clinical staff in general<br>practice for telephone and walk-in presentations</div>

<aside class="action-plan">
  <h2><span class="alert-dot">!</span>Emergency Action Plan</h2>
  <ul>
    <li>Remain calm and do not panic</li>
    <li>Be aware and respond to<br>the needs of the emergency</li>
    <li>Assess which patient needs<br>to take priority</li>
    <li>Deal with any injury or<br>illness in order of severity</li>
    <li class="call">CALL 000 <span style="font-weight:400">FOR</span><br>AMBULANCE, POLICE OR FIRE</li>
  </ul>
</aside>

<svg class="flow-lines" width="1200" height="340" aria-hidden="true">
  <g stroke="#222" stroke-width="1.3" fill="none">
    <line x1="303" y1="204" x2="168" y2="204"/>
    <line x1="447" y1="204" x2="535" y2="204"/>
    <polyline points="100,241 100,283 535,283"/>
  </g>
  <g fill="#222">
    <polygon points="162,204 170,200 170,208"/>
    <polygon points="541,204 533,200 533,208"/>
    <polygon points="541,283 533,279 533,287"/>
  </g>
</svg>
<div class="flow-question">The next available<br>appointment is…<br>Is this ok?</div>
<div class="flow-urgent">Do you have an<br>urgent problem?</div>
<span class="flow-label" style="left:186px;top:182px">No / I don’t know</span>
<span class="flow-label" style="left:488px;top:182px">Yes</span>
<span class="flow-label" style="left:222px;top:263px">No</span>

<div class="record">
  <h3>Record the patient’s phone number</h3>
  <ul>
    <li>What is the name and age of the patient?</li>
    <li>What is the nature of the problem?</li>
    <li>What is the duration of the problem?</li>
    <li>What is the severity of the problem?</li>
    <li>Has the patient had any previous major health problems?</li>
    <li>Select a category below and follow instructions.</li>
  </ul>
</div>

<section class="triage-table">
  <div class="cell head instruction">Instruction</div>
  <div class="cell head c1">CATEGORY 1</div>
  <div class="cell head c2">CATEGORY 2</div>
  <div class="cell head c3">CATEGORY 3</div>
  <div class="cell head c4">CATEGORY 4</div>
  <div class="cell head c5">CATEGORY 5</div>
  <div class="cell head c6">CATEGORY 6</div>

  <div class="cell row-label">Practice to ask the patient or caller to describe the problem(s), and categorise accordingly:</div>
  <div class="cell symptoms"><ul><li>Chest pain</li><li>Breathing difficulties/ trouble talking</li><li>Facial swelling and rash</li><li>Collapse/altered consciousness</li><li>Facial/limb weakness</li><li>Extensive burns</li><li>Sick patient you have concerns about</li></ul></div>
  <div class="cell symptoms"><ul><li>Fitting</li><li>Bleeding (heavy or persistent)</li><li>Spinal or head injury/ trauma</li><li>Snake bite</li><li>Heart palpitations</li><li>In labour/ruptured membranes</li><li>Neck stiffness/altered</li></ul></div>
  <div class="cell symptoms"><ul><li>Unable to urinate</li><li>Unwell ‘floppy’ infant</li><li>Poisoning/overdose</li><li>Eye injuries/chemical in the eye</li><li>Pain (severe)</li><li>Injured limb/possible fracture</li></ul></div>
  <div class="cell symptoms"><ul><li>Unwell child/elder with fever, vomiting, diarrhoea or pain <b>for &gt;24 hours</b></li><li>Pregnancy: pain or bleeding; reduced foetal movement</li><li>Abuse or assault</li><li>Visual disturbance</li><li>Patient or carer with extreme concern</li><li>Psychological distress</li></ul></div>
  <div class="cell symptoms"><ul><li>Unwell child/elderly with fever, vomiting, diarrhoea or pain <b>for &lt;24 hours</b></li><li>Rash (severe)</li><li>Cut/laceration</li><li>Severe flu like symptoms</li></ul></div>
  <div class="cell symptoms"><ul><li>Adult with fever, but otherwise well</li><li>Post op problems</li><li>Eye or ear infections/ pain</li><li>Adult with continuous vomiting and/or diarrhoea <b>for &gt;24 hrs</b></li></ul></div>

  <div class="cell tell row-label">Tell the caller to:</div>
  <div class="cell tell bold has-flag">Call 000<span class="flag">!</span></div>
  <div class="cell tell bold has-flag">Go to emergency department now<span class="flag">!</span></div>
  <div class="cell tell bold has-flag">Put call through to nurse/doctor<span class="flag">!</span></div>
  <div class="cell tell bold has-flag">Come to surgery now. Advise the on-call nurse/doctor<span class="flag">!</span></div>
  <div class="cell tell">Come to surgery today and call back if gets worse</div>
  <div class="cell tell">Make an appointment <b>within 24 hours</b> and call back if gets worse</div>

  <div class="cell notify row-label">Practice/<br>Receptionist</div>
  <div class="cell notify bold has-flag">Call nurse/doctor for help immediately<span class="flag">!</span></div>
  <div class="cell notify bold has-flag">Interrupt nurse/ doctor immediately<span class="flag">!</span></div>
  <div class="cell notify bold has-flag">Advise nurse/ doctor now<span class="flag">!</span></div>
  <div class="cell notify">Discuss with nurse/ doctor</div>
  <div class="cell notify">Inform nurse/doctor <b>within 30 minutes</b></div>
  <div class="cell notify">Inform nurse/doctor</div>

  <div class="cell records row-label">Practice/<br>Receptionist</div>
  <div class="cell records">Retrieve patient file<br>Document activity</div>
  <div class="cell records">Retrieve patient file<br>Document activity</div>
  <div class="cell records">Retrieve patient file<br>Document activity</div>
  <div class="cell records">Retrieve patient file<br>Document activity</div>
  <div class="cell records">Retrieve patient file<br>Document activity</div>
  <div class="cell records">Retrieve patient file<br>Document activity</div>
</section>

<footer class="footer">
  <div class="footer-mark"><span class="sq"></span>Coastal Care Alliance</div>
  <p>Whilst all care has been taken in preparing this document, this information is a guide only and subject to change without notice.<br>
  Harlow Academy produced with permissions from Coastal Care Alliance, produced by Coastal Care Alliance with Clinic Circle Eastgate with permissions from Southern Basin Careline Hub. Harlow acknowledges the FMPCB Standards Criterion 3.2.3 Practice Training and Education in Triage</p>
</footer>
</body>
</html>
```